Bilingual school website redesign

The website oruvabilingualschool.example needs a new design

It is a private school from pre kinder to third grade

They teach Spanish and English

In the same website there is a section where teachers and parents interact
Updates

Reason: We are still waiting for approval from the school's teachers.

Target Market(s)

Mostly students' parents

Industry/Entity Type

Education

Number of Pages Required

3 page

Font styles to use
Sans Serif

Requirements
Must have
• Photo gallery
• Responsive design

```html
<!DOCTYPE html>
<html lang="es">
<head>
<meta charset="utf-8">
<title>Oruva Bilingual School</title>
<link rel="stylesheet" href="https://fonts.googleapis.com/css2?family=Open+Sans:wght@400;600;700;800&family=Lilita+One&display=swap">
<style>
:root{
  --red:#d7262b;
  --red-dark:#a81519;
  --blue:#1f3f8f;
  --blue-deep:#14285e;
  --navy:#17224a;
  --sky:#8fd0f2;
  --sky-light:#d6f0fb;
  --grass:#5cae2e;
  --grey:#f0f0f0;
  --text:#444;
  --white:#fff;
}
*{box-sizing:border-box;margin:0;padding:0}
html,body{width:690px;height:1200px;overflow:hidden;background:#fff}
body{font-family:"Open Sans",Arial,sans-serif;color:var(--text)}
.page{position:relative;width:690px;height:1200px;overflow:hidden;background:#fff}
.abs{position:absolute}

/* header */
.site-header{left:0;top:0;width:690px;height:80px;background:#fff;z-index:3}
.brand{left:22px;top:8px;display:flex;align-items:center;gap:8px}
.brand-mark{width:38px;height:38px;background:var(--red);border-radius:6px}
.brand-name{font-weight:800;font-size:20px;color:var(--blue)}
.brand-sub{font-size:8px;font-weight:700;color:var(--blue);letter-spacing:.5px}
.phones{right:92px;top:6px;text-align:right}
.phones small{display:block;font-size:8px;font-weight:700;color:var(--blue)}
.phones strong{font-size:13px;color:var(--red);font-weight:800}
.phone-ico{right:238px;top:8px}
.socials{right:20px;top:8px;display:flex;gap:4px}
.socials span{width:16px;height:16px;border-radius:50%;background:var(--red)}
.main-nav{left:150px;top:56px;width:540px;height:22px;background:linear-gradient(var(--red),var(--red-dark));display:flex;align-items:center;justify-content:flex-end;padding-right:20px;gap:16px}
.main-nav a{color:#fff;font-size:8px;font-weight:700;text-decoration:none;letter-spacing:.3px}

/* hero */
.hero{left:0;top:80px;width:690px;height:222px;background:linear-gradient(var(--sky) 0%,var(--sky-light) 70%);overflow:hidden}
.grass{left:0;bottom:0;width:690px;height:40px;background:var(--grass)}
.mascot{left:20px;top:50px;width:140px;height:172px;background:radial-gradient(ellipse at 50% 45%,#8a5a2b,#5b3716);border-radius:50% 50% 12px 12px;z-index:1}
.hero-phones{left:6px;top:6px;background:var(--red);color:#fff;padding:4px 8px;transform:rotate(-4deg);border:2px solid #fff;z-index:2}
.hero-phones b{display:block;font-size:9px;font-weight:800}
.hero-phones span{display:block;font-family:"Lilita One",sans-serif;font-size:12px;line-height:1.1}
.headline{left:172px;top:6px;font-family:"Lilita One",sans-serif;color:var(--blue);font-size:44px;line-height:.95;text-shadow:2px 2px 0 #fff,-1px -1px 0 #fff;white-space:nowrap}
.headline .line2{padding-left:30px}
.headline .y{color:var(--red);font-size:40px}
.badge50{left:168px;top:92px;width:84px;height:84px;border-radius:50%;background:var(--red);border:4px solid #fff;color:#fff;font-family:"Lilita One",sans-serif;font-size:32px;display:flex;align-items:center;justify-content:center;z-index:2}
.offer{left:260px;top:96px;font-family:"Lilita One",sans-serif;color:var(--blue);font-size:29px;line-height:1.05;text-shadow:2px 2px 0 #fff;white-space:nowrap}
.valid{left:262px;top:166px;background:var(--red);color:#fff;font-weight:800;font-size:12px;padding:4px 16px;border:2px solid #fff;z-index:2;white-space:nowrap}
.crest{left:530px;top:20px;width:140px;text-align:center}
.crest-flags{width:140px;height:40px;background:linear-gradient(90deg,#3a76c9 0 45%,#fff 45% 55%,#c4262b 55%);border-radius:4px}
.crest-name{margin-top:4px;background:var(--blue);color:#fff;font-weight:800;font-size:13px;padding:4px 0}
.partner{left:596px;top:142px;width:76px;height:34px;background:#fff;border-radius:4px;z-index:1}

/* welcome */
.welcome{left:0;top:302px;width:690px;height:70px;background:linear-gradient(var(--blue),var(--blue-deep));display:flex;align-items:center;padding:0 26px;gap:22px}
.welcome h1{color:#fff;font-size:13px;font-weight:800;line-height:1.2;width:150px;flex:none}
.welcome p{color:#d7def0;font-size:7.5px;line-height:1.5}

/* columns */
.col{top:386px;width:198px;height:272px;border:1px solid #ddd;background:#fff}
.col h2{height:24px;background:linear-gradient(var(--blue),var(--blue-deep));color:#fff;font-size:11px;font-weight:800;text-align:center;line-height:24px;letter-spacing:.4px}
.services{left:26px}
.services ul{list-style:none;padding:10px 12px}
.services li{font-size:8.5px;font-weight:600;color:#333;padding:5px 0;border-bottom:1px solid #eee;display:flex;gap:6px;align-items:center}
.services li::before{content:"";width:0;height:0;border-left:5px solid var(--red);border-top:3px solid transparent;border-bottom:3px solid transparent}
.gallery{left:246px}
.gallery-photo{margin:12px;height:200px;background:linear-gradient(#c7cbbf,#8b7a64)}
.news{left:466px}
.news-item{display:flex;gap:8px;padding:10px 10px 6px;border-bottom:1px solid #eee}
.news-thumb{width:62px;height:44px;flex:none;background:linear-gradient(135deg,#f3d3d3,#9fc3e8)}
.news-item b{font-size:8.5px;color:var(--blue);line-height:1.2}
.more{position:absolute;left:10px;right:10px;bottom:10px;height:18px;background:var(--red);color:#fff;font-size:8.5px;font-weight:700;text-align:center;line-height:18px}

/* testimonials */
.testimonials{left:0;top:670px;width:690px;height:142px;background:var(--grey);text-align:center}
.testimonials h2{margin-top:14px;font-size:12px;font-weight:800;color:#333;letter-spacing:.6px}
.rule{width:40px;height:2px;background:var(--red);margin:5px auto 0}
.quote{left:110px;top:44px;width:470px;display:flex;gap:14px;text-align:left}
.avatar{width:44px;height:44px;border-radius:50%;background:#b3b7bd;flex:none;border:3px solid #fff}
.quote p{font-size:8px;font-style:italic;line-height:1.6;color:#555}
.quote cite{display:block;margin-top:6px;font-size:8px;font-weight:700;font-style:normal;color:#333}
.arrow{top:60px}

/* swoosh */
.swoosh{left:0;top:812px;width:690px;height:96px}
.swoosh-logo{left:310px;top:826px;width:70px;height:70px;border-radius:50%;background:#fff;display:flex;align-items:center;justify-content:center;font-weight:800;font-size:13px;color:var(--blue)}
.swoosh-bear{left:560px;top:826px;width:100px;height:80px;background:radial-gradient(ellipse at 50% 45%,#8a5a2b,#5b3716);border-radius:50% 50% 10px 10px}

/* footer */
.site-footer{left:0;top:906px;width:690px;height:236px;background:var(--navy);color:#fff}
.site-footer h3{position:absolute;left:26px;top:14px;font-size:15px;font-weight:800;letter-spacing:.5px}
.contact{left:26px;top:52px;width:160px}
.contact-row{display:flex;gap:8px;margin-bottom:14px}
.contact-row .ico{width:18px;height:18px;border-radius:50%;background:var(--red);flex:none;display:flex;align-items:center;justify-content:center}
.contact-row b{display:block;font-size:8px;letter-spacing:.3px}
.contact-row span{display:block;font-size:7.5px;color:#c7cde0;line-height:1.4}
.fcol-title{font-size:8px;font-weight:800;letter-spacing:.3px}
.map-col{left:200px;top:56px}
.map{margin-top:8px;width:116px;height:84px;background:linear-gradient(135deg,#e7e1cf,#c9d8b9);border:2px solid #fff}
.site-col{left:336px;top:56px}
.site-badge{margin-top:8px;width:110px;height:56px;background:#fff;display:flex;align-items:center;gap:6px;padding:6px}
.site-badge i{width:20px;height:20px;background:var(--red);flex:none}
.site-badge span{font-size:8px;font-weight:700;color:var(--blue);line-height:1.2}
.links-col{left:470px;top:56px;width:200px}
.links{display:flex;gap:20px;margin-top:8px}
.links ul{list-style:none}
.links li{font-size:7.5px;color:#c7cde0;line-height:1.9}

/* bottom */
.bottom-nav{left:0;top:1142px;width:690px;height:32px;background:#fff;display:flex;align-items:center;padding:0 26px;gap:16px}
.bottom-nav a{font-size:7.5px;font-weight:700;color:var(--blue);text-decoration:none}
.follow{margin-left:auto;display:flex;align-items:center;gap:5px;font-size:8px;font-weight:800;color:var(--blue)}
.follow span{width:14px;height:14px;border-radius:50%;background:var(--red)}
.copyright{left:0;top:1174px;width:690px;height:26px;background:var(--blue-deep);color:#c7cde0;font-size:7.5px;line-height:26px;padding-left:26px}
</style>
</head>
<body>
<div class="page">

  <header class="site-header abs">
    <div class="brand abs">
      <span class="brand-mark"></span>
      <div><div class="brand-name">Oruva</div><div class="brand-sub">BILINGUAL SCHOOL</div></div>
    </div>
    <svg class="phone-ico abs" width="18" height="18" viewBox="0 0 24 24"><circle cx="12" cy="12" r="12" fill="#1f3f8f"/><path d="M8 6l2 0 1 3-1.5 1a7 7 0 0 0 4 4l1-1.5 3 1v2a2 2 0 0 1-2 2A10 10 0 0 1 6 8a2 2 0 0 1 2-2z" fill="#fff"/></svg>
    <div class="phones abs"><small>OUR PHONES</small><strong>2200-1100, 2200-1122</strong></div>
    <div class="socials abs"><span></span><span></span><span></span></div>
    <nav class="main-nav abs">
      <a>HOME</a><a>OUR SCHOOL</a><a>NEWS</a><a>ACTIVITIES</a><a>ONLINE RESOURCES</a><a>CONTACT US</a>
    </nav>
  </header>

  <section class="hero abs">
    <div class="grass abs"></div>
    <div class="hero-phones abs"><b>TELÉFONOS:</b><span>2200-1100</span><span>2200-1122</span></div>
    <div class="mascot abs" role="img" aria-label="Mascota de la escuela, un oso con camiseta, saludando"></div>
    <div class="headline abs">“MATRÍCULA<br><span class="line2">GRATIS” <span class="y">y</span></span></div>
    <div class="badge50 abs">50%</div>
    <div class="offer abs">en tu Primer<br>Mensualidad</div>
    <div class="valid abs">Válido hasta el 31 de Agosto de 2015</div>
    <div class="crest abs">
      <div class="crest-flags" role="img" aria-label="Banderas de Honduras y Estados Unidos"></div>
      <div class="crest-name">Oruva Bilingual School</div>
    </div>
    <div class="partner abs"></div>
  </section>

  <section class="welcome abs">
    <h1>WELCOME TO<br>BILINGUAL SCHOOL</h1>
    <p>Our school welcomes children from pre kinder to third grade in a warm bilingual setting. Each day they learn, play and grow in Spanish and English with caring teachers, small classes and a safe campus where parents stay close to every step.</p>
  </section>

  <section class="col services abs">
    <h2>OUR SERVICES</h2>
    <ul>
      <li>100% Bilingual Education</li>
      <li>Full English Tests</li>
      <li>Private transportation</li>
      <li>Morning Service</li>
      <li>Latest technology</li>
      <li>Language lab</li>
      <li>Computer Lab</li>
      <li>Taekwondo Classes</li>
    </ul>
    <div class="more">More »</div>
  </section>

  <section class="col gallery abs">
    <h2>SCHOOL GALLERY</h2>
    <div class="gallery-photo" role="img" aria-label="Foto de maestras y alumnos frente a la escuela"></div>
    <div class="more">More »</div>
  </section>

  <section class="col news abs">
    <h2>LATEST NEWS</h2>
    <div class="news-item"><div class="news-thumb" role="img" aria-label="Afiche de la promoción de matrícula"></div><b>Registration Promotion</b></div>
    <div class="news-item"><div class="news-thumb" role="img" aria-label="Afiche de actividad de Pascua"></div><b>Press Here Easter</b></div>
    <div class="news-item"><div class="news-thumb" role="img" aria-label="Afiche de comunicado"></div><b>Release</b></div>
    <div class="more">More »</div>
  </section>

  <section class="testimonials abs">
    <h2>TESTIMONIALS</h2>
    <div class="rule"></div>
    <svg class="arrow abs" style="left:26px" width="12" height="20" viewBox="0 0 12 20"><path d="M10 2L2 10l8 8" stroke="#bbb" stroke-width="2" fill="none"/></svg>
    <svg class="arrow abs" style="right:26px" width="12" height="20" viewBox="0 0 12 20"><path d="M2 2l8 8-8 8" stroke="#bbb" stroke-width="2" fill="none"/></svg>
    <div class="quote abs">
      <div class="avatar" role="img" aria-label="Retrato de la madre que da el testimonio"></div>
      <div>
        <p>“Our daughter started pre kinder speaking only Spanish and now she reads simple stories in English. The teachers keep us informed every week and she runs happily to class each morning.”</p>
        <cite>— laura mejía</cite>
      </div>
    </div>
  </section>

  <svg class="swoosh abs" viewBox="0 0 690 96" preserveAspectRatio="none">
    <rect width="690" height="96" fill="#17224a"/>
    <path d="M0 0H690V40C520 10 400 70 250 50 150 36 60 20 0 40Z" fill="#f0f0f0"/>
    <path d="M0 40C60 20 150 36 250 50 400 70 520 10 690 40V56C520 28 400 88 250 68 150 54 60 38 0 58Z" fill="#1f3f8f"/>
    <path d="M0 58C60 38 150 54 250 68 400 88 520 28 690 56V62C520 36 400 94 250 74 150 60 60 44 0 64Z" fill="#d7262b"/>
  </svg>
  <div class="swoosh-logo abs">Oruva</div>
  <div class="swoosh-bear abs" role="img" aria-label="Mascota oso de la escuela"></div>

  <footer class="site-footer abs">
    <h3>GET IN TOUCH NOW!</h3>
    <div class="contact abs">
      <div class="contact-row">
        <span class="ico"><svg width="9" height="11" viewBox="0 0 10 14"><path d="M5 0a5 5 0 0 0-5 5c0 4 5 9 5 9s5-5 5-9a5 5 0 0 0-5-5zm0 7a2 2 0 1 1 0-4 2 2 0 0 1 0 4z" fill="#fff"/></svg></span>
        <div><b>ADDRESS</b><span>Colonia Los Pinos Sur<br>Frente a la farmacia central</span></div>
      </div>
      <div class="contact-row">
        <span class="ico"><svg width="10" height="10" viewBox="0 0 24 24"><path d="M5 2l4 0 2 5-3 2a11 11 0 0 0 7 7l2-3 5 2v4a3 3 0 0 1-3 3A19 19 0 0 1 2 5a3 3 0 0 1 3-3z" fill="#fff"/></svg></span>
        <div><b>PHONE</b><span>2200-1100, 2200-1122</span></div>
      </div>
      <div class="contact-row">
        <span class="ico"><svg width="10" height="8" viewBox="0 0 12 9"><rect width="12" height="9" fill="#fff"/><path d="M0 0l6 5 6-5" stroke="#d7262b" fill="none"/></svg></span>
        <div><b>EMAIL</b><span>info@oruvabilingualschool.example</span></div>
      </div>
    </div>
    <div class="map-col abs">
      <div class="fcol-title">NUESTRA DIRECCIÓN</div>
      <div class="map" role="img" aria-label="Mapa de ubicación de la escuela"></div>
    </div>
    <div class="site-col abs">
      <div class="fcol-title">SITIO WEB DEL INSTITUTO</div>
      <div class="site-badge"><i></i><span>Instituto Cultural Oruva</span></div>
    </div>
    <div class="links-col abs">
      <div class="fcol-title">QUICK LINKS</div>
      <div class="links">
        <ul><li>Inicio</li><li>Quienes Somos</li><li>Misión y Visión</li><li>Valores</li><li>Objetivos</li></ul>
        <ul><li>Contáctenos</li><li>Requisitos para Kinder</li><li>Requisitos para Preparatoria</li><li>Requisitos para Primaria</li><li>Términos y Condiciones</li></ul>
      </div>
    </div>
  </footer>

  <nav class="bottom-nav abs">
    <a>HOME</a><a>OUR SCHOOL</a><a>NEWS</a><a>ACTIVITIES</a><a>ONLINE RESOURCES</a><a>CONTACT US</a>
    <div class="follow">FOLLOW US <span></span><span></span><span></span></div>
  </nav>
  <div class="copyright abs">© 2015, Diseño y Desarrollo. All Rights Reserved</div>

</div>
</body>
</html>
```